Nirel Solutions Business Card
Stationary as well/logo for resumes, etc.
We are getting there. I need two samples...I like the black face Quorvix has going. I want the website across the bottom. I potentially want to see a black fade into a white bottom (background).
I also don't want it too busy so one color (blue) font. quorvix is close to what I am seeking
Gang,
I uploaded the files of my logo and am sorry for doing this late. What I am looking for is a business card and staionary that incorporates this. Peltcraft you are close to what I am lookign for witht he staionary- the card layout, I like tobrenik's better. In my logo there is a two tone as well, some with a black background and some with white- i want to try and explore this...

```html
<!DOCTYPE html>
<html lang="en">
<head>
<meta charset="utf-8">
<title>Nirel Solutions — Business Card</title>
<link rel="stylesheet" href="https://fonts.googleapis.com/css2?family=Tinos:ital,wght@0,400;0,700;1,400&display=swap">
<style>
  :root {
    --card-dark: #050507;
    --card-mid: #1d1c24;
    --card-light: #3e3b4c;
    --footer-navy: #0b1426;
    --accent-cyan: #3ec6dc;
    --accent-cyan-deep: #2aa9c4;
    --web-cyan: #1f8fa8;
    --text-white: #f2f2f4;
    --mark-grey: #8e9099;
  }
  html, body {
    margin: 0;
    padding: 0;
    width: 1200px;
    height: 686px;
    overflow: hidden;
    background: #ffffff;
  }
  .business-card {
    position: relative;
    width: 1200px;
    height: 686px;
    overflow: hidden;
    background: linear-gradient(100deg, var(--card-dark) 0%, var(--card-mid) 45%, var(--card-light) 100%);
    font-family: "Tinos", "Times New Roman", serif;
  }
  .brand {
    position: absolute;
    left: 60px;
    top: 30px;
    width: 300px;
    text-align: center;
  }
  .brand-mark {
    display: block;
    margin: 0 auto;
  }
  .brand-name {
    margin: 18px 0 0;
    color: var(--accent-cyan-deep);
    font-weight: 700;
    font-size: 38px;
    line-height: 1.15;
    letter-spacing: 4px;
  }
  .holder {
    position: absolute;
    left: 580px;
    top: 22px;
  }
  .holder-name {
    margin: 0;
    color: var(--accent-cyan);
    font-style: italic;
    font-weight: 400;
    font-size: 57px;
    line-height: 1;
    letter-spacing: 1px;
  }
  .holder-title {
    margin: 12px 0 0;
    color: var(--accent-cyan);
    font-style: italic;
    font-size: 41px;
    line-height: 1;
    letter-spacing: 0.5px;
  }
  .header-rule {
    position: absolute;
    left: 509px;
    top: 162px;
    width: 691px;
    height: 8px;
    background: var(--accent-cyan);
  }
  .contact {
    position: absolute;
    left: 657px;
    top: 190px;
    margin: 0;
    color: var(--text-white);
    font-style: italic;
    font-size: 36px;
    line-height: 1;
  }
  .address-line { display: block; margin-bottom: 25px; }
  .phone-line { display: block; margin-bottom: 18px; }
  .contact .address-line:nth-child(3) { margin-bottom: 38px; }
  .footer {
    position: absolute;
    left: 0;
    top: 613px;
    width: 1200px;
    height: 73px;
    background: var(--footer-navy);
    border-top: 9px solid var(--accent-cyan);
    box-sizing: border-box;
    text-align: center;
  }
  .website {
    margin: 0;
    padding-top: 4px;
    color: var(--web-cyan);
    font-style: italic;
    font-size: 48px;
    letter-spacing: 5px;
    line-height: 1.1;
  }
</style>
</head>
<body>
  <main class="business-card">
    <div class="brand">
      <svg class="brand-mark" width="200" height="200" viewBox="0 0 200 200" aria-hidden="true">
        <circle cx="100" cy="100" r="96" fill="var(--mark-grey)"/>
      </svg>
      <p class="brand-name">NIREL<br>SOLUTIONS</p>
    </div>

    <header class="holder">
      <h1 class="holder-name">Dorian K. Vaselli</h1>
      <p class="holder-title">Business Developer Manager.</p>
    </header>
    <div class="header-rule"></div>

    <address class="contact">
      <span class="address-line">1870 Marrow Lane South</span>
      <span class="address-line">Suite 310</span>
      <span class="address-line">Lakeport, TX &nbsp;77094</span>
      <span class="phone-line">P : 555. 214. 7380</span>
      <span class="phone-line">C : 555. 386. 1947</span>
      <span class="phone-line">F : 555. 602. 5318</span>
      <span class="phone-line">E : dorian@nirel-it.com</span>
    </address>

    <footer class="footer">
      <p class="website">www.nirel-it.com</p>
    </footer>
  </main>
</body>
</html>
```